Give us a remarkable appearance

We need a unique, remarkable stationery design (Business Cards, Business Letters, Email Signature etc.). The design should use our logo.

Verlan-Consulting is a startup in consulting, management and IT services and individual software development for the financial industry.

Verlan in english is agate stone. We would like to see designs that use colors out of the agate stone color range.

Preferred COLORS: gold, dark red (burgundy), white, dark grey, black ** see attached Logos **

The used font should be available for further usage with texts etc.

The design should express: modernity, precious, high quality, lightness, stability, ecological awareness, speedy, reliability, simplicity, sustainability.

Target Market(s)

C-Level and Business Clients, Professionals

Industry/Entity Type

Business

Logo Text

Logo styles of interest
Pictorial/Combination Logo
Abstract Logo
Wordmark Logo
Requirements
Must have
• Business Cards, Business Papers, Email Signature
Nice to have
• Door plate, Flyersheet (basic structure), Envelop...

```html
<!DOCTYPE html>
<html lang="en">
<head>
<meta charset="utf-8">
<title>Verlan Consulting – Stationery</title>
<link rel="stylesheet" href="https://fonts.googleapis.com/css2?family=Jost:wght@400;500;600;700&display=swap">
<style>
  :root {
    --gold: #d9a514;
    --gold-light: #f5c400;
    --gold-dark: #b3842a;
    --ink: #3a3a3a;
    --ink-soft: #6b6b6b;
    --paper: #ffffff;
    --paper-shade: #f1f1f1;
    --stage: #e4e4e4;
  }
  * { margin: 0; padding: 0; box-sizing: border-box; }
  html, body { width: 1200px; height: 808px; overflow: hidden; }
  body {
    position: relative;
    background: var(--stage);
    font-family: "Jost", "Futura", sans-serif;
    color: var(--ink);
  }
  .sheet {
    position: absolute;
    background: var(--paper);
    box-shadow: 0 2px 8px rgba(0,0,0,.18);
  }
  .brand {
    display: flex;
    align-items: center;
    gap: 8px;
    font-weight: 700;
    color: var(--gold);
    line-height: 1;
    white-space: nowrap;
  }
  .brand-square {
    width: 0.9em;
    height: 0.9em;
    background: var(--gold);
  }
  .brand--light { color: var(--paper); }
  .brand--light .brand-square { background: var(--paper); }

  .contact { font-size: 7px; line-height: 1.5; color: var(--ink); }
  .contact-line { display: flex; align-items: center; gap: 3px; }
  .contact strong { font-weight: 600; }
  .icon { width: 7px; height: 7px; flex: none; }
  .web { font-size: 8px; font-weight: 500; color: var(--ink); }

  /* Letterhead */
  .letterhead { left: 30px; top: 19px; width: 545px; height: 770px; }
  .letterhead .brand { position: absolute; left: 48px; top: 118px; font-size: 26px; }
  .letterhead .contact { position: absolute; left: 390px; top: 52px; }
  .letterhead .web { position: absolute; left: 48px; bottom: 34px; }

  /* Business cards */
  .card { width: 270px; height: 155px; top: 30px; }
  .card-front { left: 610px; }
  .card-front .brand { position: absolute; left: 22px; top: 26px; font-size: 17px; }
  .card-front .person { position: absolute; left: 22px; top: 78px; }
  .person-name { font-size: 9px; font-weight: 600; color: var(--gold); }
  .person-role { font-size: 7px; color: var(--ink-soft); font-weight: 400; }
  .card-front .contact { position: absolute; left: 22px; top: 96px; }
  .card-back {
    left: 900px;
    background: radial-gradient(ellipse at 40% 35%, var(--gold-light) 0%, var(--gold) 35%, var(--gold-dark) 100%);
  }
  .card-back .brand { position: absolute; left: 50%; top: 56px; transform: translateX(-50%); font-size: 18px; }
  .card-back .web { position: absolute; right: 30px; bottom: 22px; color: var(--paper); font-size: 7px; }

  /* Envelope front */
  .envelope-front { left: 610px; top: 215px; width: 560px; height: 270px; }
  .envelope-front .brand { position: absolute; left: 58px; top: 56px; font-size: 22px; }
  .window {
    position: absolute; left: 72px; top: 128px; width: 272px; height: 80px;
    border-radius: 12px; background: var(--paper-shade);
    border: 1px solid #e2e2e2;
  }
  .envelope-front .web { position: absolute; left: 88px; bottom: 28px; font-size: 7px; }

  /* Envelope back */
  .envelope-back { left: 610px; top: 510px; width: 560px; height: 270px; overflow: hidden; }
  .flap { position: absolute; inset: 0; width: 100%; height: 100%; }
  .envelope-back .brand { position: absolute; left: 50%; top: 38px; transform: translateX(-50%); font-size: 18px; }
  .envelope-back .contact { position: absolute; right: 34px; bottom: 30px; text-align: right; }
  .envelope-back .contact-row { display: flex; gap: 6px; justify-content: flex-end; }
</style>
</head>
<body>
<svg width="0" height="0" style="position:absolute">
  <defs>
    <symbol id="icon-phone" viewBox="0 0 10 10"><circle cx="5" cy="5" r="5" fill="#d9a514"/><path d="M3 3.2c.3-.4.7-.4.9 0l.4.7c.1.3 0 .5-.2.6.3.7.8 1.2 1.4 1.5.1-.2.3-.3.6-.2l.7.4c.4.2.4.6 0 .9-.9.8-4.6-2.6-3.8-3.9z" fill="#fff"/></symbol>
    <symbol id="icon-mail" viewBox="0 0 10 10"><circle cx="5" cy="5" r="5" fill="#d9a514"/><rect x="2.4" y="3.2" width="5.2" height="3.6" fill="#fff"/><path d="M2.4 3.2 5 5.3 7.6 3.2" stroke="#d9a514" stroke-width=".6" fill="none"/></symbol>
    <linearGradient id="flap-gold" x1="0" x2="1" y1="0" y2="0">
      <stop offset="0" stop-color="#b3842a"/>
      <stop offset=".6" stop-color="#e0b010"/>
      <stop offset=".8" stop-color="#f5c400"/>
      <stop offset="1" stop-color="#c99524"/>
    </linearGradient>
  </defs>
</svg>

<section class="sheet letterhead">
  <div class="contact">
    <strong>123, Your Street, Your City,<br>Country, 123.</strong>
    <div class="contact-line"><svg class="icon"><use href="#icon-phone"/></svg>(123) 456 7890</div>
    <div class="contact-line"><svg class="icon"><use href="#icon-phone"/></svg>(123) 456 7890</div>
    <div class="contact-line"><svg class="icon"><use href="#icon-mail"/></svg>info@verlanconsulting.com</div>
  </div>
  <div class="brand"><span class="brand-square"></span>Verlan consulting</div>
  <div class="web">verlanconsulting.com</div>
</section>

<section class="sheet card card-front">
  <div class="brand"><span class="brand-square"></span>Verlan consulting</div>
  <div class="person"><span class="person-name">Daniel Weber</span> <span class="person-role">| Publisher</span></div>
  <div class="contact">
    <strong>123, Your Street, Your City, Country, 123.</strong>
    <div class="contact-line"><svg class="icon"><use href="#icon-phone"/></svg>(123) 456 7811 <svg class="icon"><use href="#icon-phone"/></svg>(123) 456 7822</div>
    <div class="contact-line"><svg class="icon"><use href="#icon-mail"/></svg>d.weber@verlanconsulting.com</div>
  </div>
</section>

<section class="sheet card card-back">
  <div class="brand brand--light"><span class="brand-square"></span>Verlan</div>
  <div class="web">www.verlanconsulting.com</div>
</section>

<section class="sheet envelope-front">
  <div class="brand"><span class="brand-square"></span>Verlan consulting</div>
  <div class="window"></div>
  <div class="web">verlanconsulting.com</div>
</section>

<section class="sheet envelope-back">
  <svg class="flap" viewBox="0 0 560 270" preserveAspectRatio="none">
    <path d="M0 100 L280 200 L560 100" stroke="#cfcfcf" stroke-width="1" fill="none"/>
    <path d="M0 0 H560 V30 Q520 110 330 130 Q120 150 0 120 Z" fill="url(#flap-gold)"/>
  </svg>
  <div class="brand brand--light"><span class="brand-square"></span>Verlan</div>
  <div class="contact">
    <strong>123, Your Street, Your City, Country, 123.</strong>
    <div class="contact-row">
      <span class="contact-line"><svg class="icon"><use href="#icon-phone"/></svg>(123) 456 7890</span>
      <span class="contact-line"><svg class="icon"><use href="#icon-phone"/></svg>(123) 456 7890</span>
      <span class="contact-line"><svg class="icon"><use href="#icon-mail"/></svg>info@verlanconsulting.com</span>
    </div>
  </div>
</section>
</body>
</html>
```